Need a small Brochure Designing for a High Tech LED Spotlight

This is an expensive product and the best of it's kind in the world, so it needs to be marketed to intelligent, forward thinking people who appreciate and pay for excellent design and innovation. The type of people who buy Quince products i guess. It needs to be clean. The colours do not need to be in keep with our website, but our logo does need to be on the brochure. I have attached a dcoument with all the text, the order the text goes in and an idea of how i want the first page to look. All images and logos have been attached too.

Target Market(s)

This is aimed at people with high disposible incomes who spend money on the best designed products and the latest technology. The type of people who buy Quince products.

Industry/Entity Type

Product

Requirements
Must have
• The work needs to be editable by us using indesign

The pages need to be A5. I'm not sure how many pages the brochure needs to be as it does need to be clean and be spaced out well. On the file that contains the text i've indicated that 8 pages would be good.

The logos i attached - 1) Kelo Product Design Award, 2) Z Technology Award, 3) Blue Fern Design Award and 4) Keen Design Award all need to be at the bottom of the front page, quite small, but still able to see them well.

- Needs to have a QR code so that smart phones can scan the code and be taken to a pol vane clip - QR code is attached.
- Needs to have Plimbo Icon - @KestrowHomeCo
Nice to have
• Nice to remind customers on each page that the product has a 5 year Warranty and we have a 365 day Returns Policy.

```html
<!DOCTYPE html>
<html lang="en">
<head>
<meta charset="utf-8">
<title>Q5 6w LED Spotlight Brochure</title>
<link href="https://fonts.googleapis.com/css2?family=Raleway:wght@200;300;400;700&display=swap" rel="stylesheet">
<style>
  :root {
    --stage-top: #9a9a9a;
    --stage-mid: #bdbdbd;
    --stage-low: #dcdcdc;
    --paper: #f4f3f2;
    --paper-shade: #e6e5e4;
    --ink: #3a3a3a;
    --ink-soft: #6b6b6b;
    --ink-strong: #111111;
    --band: rgba(255,255,255,0.55);
  }
  * { box-sizing: border-box; margin: 0; padding: 0; }
  html, body { width: 726px; height: 1200px; overflow: hidden; }
  body {
    position: relative;
    font-family: "Raleway", sans-serif;
    color: var(--ink);
    background: linear-gradient(180deg, var(--stage-top) 0%, var(--stage-mid) 40%, var(--stage-low) 100%);
  }
  .page { position: absolute; background: var(--paper); box-shadow: 0 2px 8px rgba(0,0,0,0.18); overflow: hidden; }

  /* Cover */
  .cover { left: 162px; top: 40px; width: 402px; height: 568px;
    background: linear-gradient(180deg, #f2f1f0 0%, #ebeae9 100%); }
  .cover-title { position: absolute; top: 72px; width: 100%; text-align: center;
    font-weight: 200; font-size: 44px; letter-spacing: 2px; color: var(--ink); }
  .cover-tagline { position: absolute; top: 150px; width: 100%; text-align: center;
    font-weight: 200; font-size: 13px; line-height: 1.3; color: var(--ink); }
  .cover-product { position: absolute; left: 60px; top: 210px; width: 300px; height: 300px;
    background: radial-gradient(circle at 42% 45%, #f3ecd8 0%, #d8caa0 18%, #a89463 34%, #d9d5cd 52%, rgba(235,234,233,0) 70%); }
  .cover-note { position: absolute; right: 34px; bottom: 24px; font-size: 6px; color: var(--ink-soft); }

  /* Spread */
  .spread-left { left: 105px; top: 700px; width: 262px; height: 440px;
    background: linear-gradient(90deg, #f6f6f6 0%, #efefef 85%, var(--paper-shade) 100%); }
  .spread-left svg { position: absolute; inset: 0; }
  .spread-heading { position: absolute; top: 36px; right: 14px; width: 230px; text-align: right;
    font-weight: 300; font-size: 14px; line-height: 1.3; color: var(--ink); }
  .spread-copy { position: absolute; left: 28px; top: 108px; width: 222px; font-size: 6px; line-height: 1.45; }
  .spread-copy p { margin-bottom: 8px; color: var(--ink-soft); }
  .spread-copy .lead { font-weight: 700; font-size: 7px; color: var(--ink-strong); margin-bottom: 12px; }
  .spread-copy .quote { font-weight: 700; color: var(--ink-strong); margin-top: 6px; }

  .spread-right { left: 367px; top: 700px; width: 313px; height: 430px;
    background: linear-gradient(90deg, var(--paper-shade) 0%, #f7f7f7 10%); }
  .spread-photo { position: absolute; left: 0; top: 5px; width: 308px; height: 390px;
    background: linear-gradient(180deg, #dcd6cc 0%, #ece8e2 45%, #c8a079 85%, #b88a5e 100%); }
  .spread-caption { position: absolute; bottom: 14px; width: 100%; text-align: center;
    font-size: 6px; color: var(--ink-soft); }
</style>
</head>
<body>

  <section class="page cover" aria-label="Brochure cover">
    <h1 class="cover-title">Q5 6w</h1>
    <p class="cover-tagline">You Wont Have To Replace This<br>LED Spotlight For 18 Years!*</p>
    <div class="cover-product" role="img" aria-label="Product photograph of the LED spotlight with gold finned heat sink and its reflection"></div>
    <p class="cover-note">* read the reference section</p>
  </section>

  <section class="page spread-left" aria-label="Inside page with product story">
    <svg width="262" height="440" viewBox="0 0 262 440" aria-hidden="true">
      <polygon points="0,0 70,0 262,300 262,360" fill="var(--band)"/>
      <polygon points="120,0 160,0 262,150 262,200" fill="var(--band)"/>
    </svg>
    <h2 class="spread-heading">Cut your energy consumption<br>by up to 90%</h2>
    <div class="spread-copy">
      <p class="lead">With its unrivalled performance and quality, the Q5 6w is the most technologically advanced LED Spotlight in the world.</p>
      <p>Brightmere Lighting Managing Director Dana Morrow talks about the Q5 6w LED Spot:</p>
      <p>We began working with lighting engineers in 2009. They have since built a range of lamps that pair safety and efficiency with a careful, honest approach to form and detail.</p>
      <p>This product has won a number of global design awards, such as the Kelo Product Design Award, the Z Technology Award, the Blue Fern Design Award and the Keen Design Award.</p>
      <p>In an industry where cost often wins, they remain the first choice for people who care about lighting. Their approach mirrors Quince: a rare blend of beautifully designed goods and the idea of the correct tool.</p>
      <p class="quote">"The Q5 Is The Ultimate In Lighting For The Discerning Design Conscious And Forward Thinking Person"</p>
    </div>
  </section>

  <section class="page spread-right" aria-label="Inside page with interior photograph">
    <div class="spread-photo" role="img" aria-label="Photograph of a bright modern kitchen with pendant lights, white island bench and timber floor lit by LED spotlights"></div>
    <p class="spread-caption">This product has a 5 Year Warranty and 365 Day Returns Policy</p>
  </section>

</body>
</html>
```